Business card design for my trucking company

I would like a business card designed for my new trucking company. Please use my logo. the rest of the design is up to you. i would like my clients to say wow when they see the card. Im looking forward to seeing your designs

Target Market(s)

Industry/Entity Type

Trucking Company

Contact Information for Business Card

Marcus Tillbrook President
518-555-0147
ridgelinehaulingcompany@postvane.com

Font styles to use
Serif

Requirements
Must have
• my logo, name and number. we are located in Schenectady New York. the rest is up to you
Nice to have
• up to you
Should not have
• none

```html
<!DOCTYPE html>
<html lang="en">
<head>
<meta charset="utf-8">
<title>Ridgeline Hauling &amp; Logistics – Business Cards</title>
<link href="https://fonts.googleapis.com/css2?family=Domine:wght@400;600;700&display=swap" rel="stylesheet">
<style>
  :root {
    --stage-red: #8a0006;
    --stage-navy: #0c1c5e;
    --card-red: #e31b23;
    --card-white: #ffffff;
    --card-blue: #0a4fa8;
    --card-orange: #ec7418;
    --ink-dark: #1b0d0e;
    --ink-navy: #0b1a4a;
    --ink-white: #ffffff;
    --accent-orange: #f07a1a;
  }
  * { box-sizing: border-box; margin: 0; padding: 0; }
  html, body { width: 894px; height: 1200px; overflow: hidden; }
  body { font-family: "Domine", Georgia, serif; }

  .canvas { width: 894px; height: 1200px; display: flex; flex-direction: column; }
  .colorway {
    height: 600px;
    display: flex; flex-direction: column; align-items: center; justify-content: center;
    gap: 28px;
  }
  .colorway--red { background: var(--stage-red); }
  .colorway--navy { background: var(--stage-navy); }

  .card {
    width: 380px; height: 217px; position: relative;
    box-shadow: 0 10px 24px rgba(0,0,0,.35);
  }
  .card--front { padding: 24px 26px; }
  .card--red { background: var(--card-red); }
  .card--white { background: var(--card-white); }
  .card--blue { background: var(--card-blue); }
  .card--orange { background: var(--card-orange); }

  .person-name { font-size: 19px; font-weight: 600; line-height: 1.1; }
  .person-title { font-size: 13px; color: var(--ink-white); margin-top: 3px; }
  .card--red .person-name { color: var(--ink-dark); }
  .card--blue .person-name { color: var(--accent-orange); }

  .front-brand {
    position: absolute; right: 26px; top: 86px;
    display: flex; align-items: center; gap: 10px;
  }
  .front-brand__mark { width: 30px; height: 30px; flex: none; }
  .front-brand__name {
    font-size: 15px; font-weight: 700; line-height: 1.2; text-transform: uppercase;
    letter-spacing: .5px; text-align: right;
  }
  .card--red .front-brand__mark { background: var(--ink-dark); }
  .card--red .front-brand__name { color: var(--ink-dark); }
  .card--blue .front-brand__mark { background: var(--ink-navy); }
  .card--blue .front-brand__name { color: var(--ink-navy); }

  .contact-list { position: absolute; left: 26px; bottom: 22px; list-style: none; }
  .contact-item {
    display: flex; align-items: center; gap: 8px;
    font-size: 11px; color: var(--ink-white); line-height: 1.9;
  }
  .contact-icon { width: 13px; height: 13px; flex: none; }
  .card--red .contact-icon { fill: var(--ink-dark); }
  .card--blue .contact-icon { fill: var(--accent-orange); }

  .card--back { display: flex; align-items: center; justify-content: center; gap: 14px; }
  .brand-mark { width: 44px; height: 44px; border-radius: 50%; flex: none; }
  .brand-name {
    font-size: 24px; font-weight: 700; line-height: 1.15; text-transform: uppercase;
    letter-spacing: .5px;
  }
  .card--white .brand-mark { background: var(--card-red); }
  .card--white .brand-name { color: var(--card-red); }
  .card--orange .brand-mark { background: var(--ink-navy); }
  .card--orange .brand-name { color: var(--ink-navy); }
</style>
</head>
<body>
<main class="canvas">

  <section class="colorway colorway--red">
    <article class="card card--front card--red">
      <h1 class="person-name">Marcus Tillbrook</h1>
      <p class="person-title">President</p>
      <div class="front-brand">
        <p class="front-brand__name">Ridgeline Hauling<br>&amp; Logistics Inc.</p>
        <span class="front-brand__mark" aria-hidden="true"></span>
      </div>
      <ul class="contact-list">
        <li class="contact-item">
          <svg class="contact-icon" viewBox="0 0 24 24" aria-hidden="true"><path d="M6.6 10.8a15 15 0 0 0 6.6 6.6l2.2-2.2c.3-.3.7-.4 1-.2 1.1.4 2.3.6 3.6.6.6 0 1 .4 1 1V20c0 .6-.4 1-1 1A17 17 0 0 1 3 4c0-.6.4-1 1-1h3.5c.6 0 1 .4 1 1 0 1.3.2 2.5.6 3.6.1.3 0 .7-.2 1z"/></svg>
          518-555-0147
        </li>
        <li class="contact-item">
          <svg class="contact-icon" viewBox="0 0 24 24" aria-hidden="true"><path d="M2 5h20v14H2z M2 5l10 8 10-8"/></svg>
          ridgelinehaulingcompany@postvane.com
        </li>
      </ul>
    </article>
    <article class="card card--back card--white">
      <span class="brand-mark" aria-hidden="true"></span>
      <p class="brand-name">Ridgeline Hauling<br>&amp; Logistics Inc.</p>
    </article>
  </section>

  <section class="colorway colorway--navy">
    <article class="card card--front card--blue">
      <h1 class="person-name">Marcus Tillbrook</h1>
      <p class="person-title">President</p>
      <div class="front-brand">
        <p class="front-brand__name">Ridgeline Hauling<br>&amp; Logistics Inc.</p>
        <span class="front-brand__mark" aria-hidden="true"></span>
      </div>
      <ul class="contact-list">
        <li class="contact-item">
          <svg class="contact-icon" viewBox="0 0 24 24" aria-hidden="true"><path d="M6.6 10.8a15 15 0 0 0 6.6 6.6l2.2-2.2c.3-.3.7-.4 1-.2 1.1.4 2.3.6 3.6.6.6 0 1 .4 1 1V20c0 .6-.4 1-1 1A17 17 0 0 1 3 4c0-.6.4-1 1-1h3.5c.6 0 1 .4 1 1 0 1.3.2 2.5.6 3.6.1.3 0 .7-.2 1z"/></svg>
          518-555-0147
        </li>
        <li class="contact-item">
          <svg class="contact-icon" viewBox="0 0 24 24" aria-hidden="true"><path d="M2 5h20v14H2z M2 5l10 8 10-8"/></svg>
          ridgelinehaulingcompany@postvane.com
        </li>
      </ul>
    </article>
    <article class="card card--back card--orange">
      <span class="brand-mark" aria-hidden="true"></span>
      <p class="brand-name">Ridgeline Hauling<br>&amp; Logistics Inc.</p>
    </article>
  </section>

</main>
</body>
</html>
```